Bright Fern Custom Homes business card. Double sided. Modern. professional

Bright Fern Custom Homes
contemporary modern design with our logo /
Double sided with all our contact information
Use same Green colors as in our Logo. Contemporary logo that grabs your attention. Visually pleasing and balanced. Easy to read, and Vibrant. Would love an option for rounded edges. Embossed logo would be amazing.
Contact Information for Business Card
Dana Welk Owner / General Contractor Bright Fern Custom Homes p: 704.552.1830 m: 912.648.2071 e: brightferncustomhomes@mailbox.example w: www.brightferncustomhomes.example 218 Pryor Meadow Lane Batesburg, SC 29041

```html
<!DOCTYPE html>
<html lang="en">
<head>
<meta charset="utf-8">
<title>Bright Fern Custom Homes – Business Card</title>
<link href="https://fonts.googleapis.com/css2?family=Ubuntu:wght@300;400;500;700&display=swap" rel="stylesheet">
<style>
  :root {
    --backdrop: #e4e5e8;
    --fern-dark: #44591f;
    --fern: #5f7a32;
    --fern-light: #6b8540;
    --fern-accent: #6a8a2a;
    --emboss: #4e6826;
    --card-white: #ffffff;
    --card-edge: #efefef;
    --ink: #555555;
    --ink-strong: #5a5a5a;
  }
  * { margin: 0; padding: 0; box-sizing: border-box; }
  html, body { width: 1200px; height: 824px; overflow: hidden; }
  body {
    background: var(--backdrop);
    font-family: "Ubuntu", sans-serif;
    position: relative;
  }
  .card {
    position: absolute;
    left: 384px;
    width: 432px;
    height: 246px;
    border-radius: 12px;
    overflow: hidden;
  }
  .card-front {
    top: 134px;
    background: linear-gradient(30deg, var(--fern-dark) 0%, var(--fern) 55%, var(--fern-light) 100%);
  }
  .front-brand {
    position: absolute;
    left: 0; right: 0;
    top: 104px;
    text-align: center;
    font-size: 24px;
    font-weight: 500;
    color: var(--emboss);
    letter-spacing: 0.5px;
  }
  .front-web {
    position: absolute;
    left: 0; right: 0;
    top: 216px;
    text-align: center;
    font-size: 9.6px;
    color: #f2f5ea;
    letter-spacing: 0.2px;
  }
  .card-back {
    top: 443px;
    background: radial-gradient(ellipse at 70% 40%, var(--card-white) 40%, var(--card-edge) 100%);
  }
  .back-brand {
    position: absolute;
    left: 22px;
    width: 150px;
    top: 112px;
    display: flex;
    flex-direction: column;
    align-items: center;
    gap: 8px;
    text-align: center;
    font-size: 15px;
    font-weight: 500;
    line-height: 1.2;
    color: var(--fern-accent);
  }
  .back-brand .mark {
    width: 14px; height: 14px;
    border-radius: 50%;
    background: var(--fern-accent);
  }
  .holder {
    position: absolute;
    left: 208px;
    top: 40px;
    border-left: 3px solid var(--fern-accent);
    padding-left: 5px;
  }
  .holder-name {
    font-size: 25px;
    line-height: 24px;
    font-weight: 300;
    color: var(--ink-strong);
  }
  .holder-name strong { font-weight: 500; }
  .holder-role {
    font-size: 15px;
    line-height: 18px;
    color: var(--fern-accent);
  }
  .contact {
    position: absolute;
    left: 209px;
    list-style: none;
    font-size: 10px;
    color: var(--ink);
  }
  .contact li { display: flex; align-items: flex-start; gap: 4px; line-height: 12.5px; }
  .contact svg { flex: none; width: 8px; height: 8px; margin-top: 2.5px; }
  .contact-address { top: 118px; }
  .contact-lines { top: 162px; }
  .icon { fill: none; stroke: var(--fern-accent); stroke-width: 1.3; }
  .icon-fill { fill: var(--fern-accent); }
</style>
</head>
<body>

<section class="card card-front" aria-label="Card front">
  <div class="front-brand">Bright Fern Custom Homes</div>
  <div class="front-web">www.brightferncustomhomes.example</div>
</section>

<section class="card card-back" aria-label="Card back">
  <div class="back-brand"><span class="mark"></span><span>Bright Fern<br>Custom Homes</span></div>

  <div class="holder">
    <div class="holder-name">Dana <strong>Welk</strong></div>
    <div class="holder-role">Owner</div>
  </div>

  <ul class="contact contact-address">
    <li>
      <svg viewBox="0 0 8 8"><path class="icon" d="M4 7.5 C2 5 1.2 3.8 1.2 2.9 A2.8 2.8 0 0 1 6.8 2.9 C6.8 3.8 6 5 4 7.5Z"/><circle class="icon-fill" cx="4" cy="3" r="0.9"/></svg>
      <span>218 Pryor Meadow Lane<br>Cedarvale, SC 29041</span>
    </li>
  </ul>

  <ul class="contact contact-lines">
    <li>
      <svg viewBox="0 0 8 8"><path class="icon" d="M1.5 1 L3 1 L3.6 2.8 L2.7 3.5 C3.2 4.6 3.9 5.3 4.9 5.8 L5.6 4.9 L7.2 5.5 L7.2 7 C4 7 1 4.2 1.5 1Z"/></svg>
      <span>704.552.1830</span>
    </li>
    <li>
      <svg viewBox="0 0 8 8"><rect class="icon" x="2" y="0.7" width="4" height="6.6" rx="0.7"/><circle class="icon-fill" cx="4" cy="6.2" r="0.5"/></svg>
      <span>912.648.2071</span>
    </li>
    <li>
      <svg viewBox="0 0 8 8"><rect class="icon-fill" x="0.8" y="2" width="6.4" height="4.2"/><path d="M0.8 2 L4 4.4 L7.2 2" fill="none" stroke="#fff" stroke-width="0.7"/></svg>
      <span>brightferncustomhomes@mailbox.example</span>
    </li>
    <li>
      <svg viewBox="0 0 8 8"><circle class="icon" cx="4" cy="4" r="3"/><path class="icon" d="M1 4 H7 M4 1 C2.5 3 2.5 5 4 7 M4 1 C5.5 3 5.5 5 4 7" stroke-width="0.7"/></svg>
      <span>www.brightferncustomhomes.example</span>
    </li>
  </ul>
</section>

</body>
</html>
```